Professional Photography Business cards

I need business cards that include my logo which I have uploaded. I run a photography business. I am open to ideas but I would like one side to have my logo and the other side to have my contact info. I don't have a website made but I do own a website domain. I have uploaded 2 different logo color schemes. My business colors are Blue, black , and white.

Business Name
Business Phone Number
Business Email
Business Website address
Instagram

Industry/Entity Type

Professional Photography

Contact Information for Business Card

Phone Number: 555-314-8027 email: info@tkellan-studios.example Instagram: @t.kellanstudios website doman- www.tkellan-studios.example

Requirements
Must have
• I like the idea of a business card with a full black background front and back of card. My colors must include royal blue, black, and white

```html
<!DOCTYPE html>
<html lang="en">
<head>
<meta charset="utf-8">
<title>T. Kellan Studios – Business Cards</title>
<link href="https://fonts.googleapis.com/css2?family=Arimo:wght@400;700&display=swap" rel="stylesheet">
<style>
  :root {
    --backdrop: #2b2b2d;
    --card: #050505;
    --royal-blue: #1418b8;
    --white: #ffffff;
    --faint: #141414;
  }
  * { box-sizing: border-box; margin: 0; padding: 0; }
  html, body {
    width: 1200px; height: 1015px; overflow: hidden;
    background: var(--backdrop);
    font-family: "Arimo", Arial, sans-serif;
  }
  .sheet {
    width: 1200px; height: 1015px;
    display: flex; flex-direction: column; align-items: center; justify-content: center;
    gap: 56px;
  }
  .card {
    position: relative;
    width: 740px; height: 423px;
    background: var(--card);
    border-radius: 4px;
    box-shadow: 0 14px 40px rgba(0,0,0,.55);
    overflow: hidden;
  }
  .card__motif {
    position: absolute;
    border-radius: 50%;
    border: 22px solid var(--faint);
  }
  .card--front .card__motif { width: 330px; height: 330px; left: 340px; top: 20px; }
  .card--back .card__motif { width: 300px; height: 300px; left: 170px; top: 110px; }

  .brand {
    position: absolute; display: flex; align-items: center; gap: 14px;
    color: var(--royal-blue); font-weight: 700; letter-spacing: .5px;
  }
  .brand__dot { border-radius: 50%; background: var(--white); flex: none; }
  .card--front .brand { left: 50%; top: 50%; transform: translate(-50%, -50%); font-size: 58px; }
  .card--front .brand__dot { width: 30px; height: 30px; }
  .card--back .brand { right: 44px; top: 48px; font-size: 34px; }
  .card--back .brand__dot { width: 20px; height: 20px; }

  .social {
    position: absolute; right: 44px; top: 190px;
    display: flex; align-items: center; gap: 10px;
    color: var(--white); font-size: 19px;
  }
  .social__mark { width: 20px; height: 20px; border-radius: 50%; background: var(--royal-blue); }

  .contact {
    position: absolute; left: 44px; bottom: 40px;
    list-style: none; display: flex; flex-direction: column; gap: 10px;
    color: var(--white); font-size: 19px;
  }
  .contact__item { display: flex; align-items: center; gap: 12px; }
  .contact__icon {
    width: 26px; height: 26px; border-radius: 50%; background: var(--royal-blue);
    display: flex; align-items: center; justify-content: center; flex: none;
  }
  .contact__icon svg { width: 14px; height: 14px; }
</style>
</head>
<body>
<main class="sheet">
  <section class="card card--front" aria-label="Card front">
    <div class="card__motif" aria-hidden="true"></div>
    <div class="brand"><span class="brand__dot"></span>T. Kellan Studios</div>
  </section>

  <section class="card card--back" aria-label="Card back">
    <div class="card__motif" aria-hidden="true"></div>
    <div class="brand"><span class="brand__dot"></span>T. Kellan Studios</div>
    <div class="social"><span>@t.kellanstudios</span><span class="social__mark"></span></div>
    <ul class="contact">
      <li class="contact__item">
        <span class="contact__icon">
          <svg viewBox="0 0 24 24" fill="#fff"><path d="M6.6 10.8a15.1 15.1 0 0 0 6.6 6.6l2.2-2.2a1 1 0 0 1 1-.25 11.4 11.4 0 0 0 3.6.57 1 1 0 0 1 1 1V20a1 1 0 0 1-1 1A17 17 0 0 1 3 4a1 1 0 0 1 1-1h3.5a1 1 0 0 1 1 1c0 1.25.2 2.45.57 3.57a1 1 0 0 1-.25 1z"/></svg>
        </span>555-314-8027
      </li>
      <li class="contact__item">
        <span class="contact__icon">
          <svg viewBox="0 0 24 24" fill="none" stroke="#fff" stroke-width="2"><rect x="3" y="5" width="18" height="14" rx="1"/><path d="M3 6l9 7 9-7"/></svg>
        </span>info@tkellan-studios.example
      </li>
      <li class="contact__item">
        <span class="contact__icon">
          <svg viewBox="0 0 24 24" fill="none" stroke="#fff" stroke-width="2"><circle cx="12" cy="12" r="9"/><path d="M3 12h18M12 3c3 3 3 15 0 18M12 3c-3 3-3 15 0 18"/></svg>
        </span>www.tkellan-studios.example
      </li>
    </ul>
  </section>
</main>
</body>
</html>
```